Tulven Electrics Flyer Design Advertising

I am after an A5 Flyer design to help promote my electrical services business.
I would like to have information on what my business offers, photos of electrical work, and specials/deals for an amount of time.

Industry/Entity Type

Electrician

Font styles to use
Sans Serif

Colors
0292cd
33a6d7
85cae6
3176b5
333333
1b1b1b
ffffff
5c5c5c
474747

Requirements
Must have
• Specialising in New homes, renovations and commercial projects
• Contact details:
• ph. 0437 619 458
• email admin@tulvenelectrics.example.au
• facebook TulvenElectrics
• Specials/Deals:
• 10% off all electrical services
• or
• Free LED downlights on installation
• *Terms conditions apply
• ALL RESIDENTIAL & COMMERCIAL ELECTRICAL SERVICES
• - New Home installations
• - Commercial projects
• - Shop fit outs
• - Renovations
• - Smoke Detectors
• - Air Conditioning and Ceiling Fans
• - Garden Lighting
• - Oven and Cooktop Installations
• - Power Point installation
• - LED lighting upgrades
• - Security Lighting
• - Switchboard upgrades
• - Test and Tag
• - Commercial Property
• - General Electrical Maintenance

```html
<!DOCTYPE html>
<html lang="en">
<head>
<meta charset="utf-8">
<title>Tulven Electrics Flyer</title>
<link rel="stylesheet" href="https://fonts.googleapis.com/css2?family=Lato:wght@400;700&family=Roboto+Condensed:wght@500;700&family=Arimo:wght@400;700&display=swap">
<style>
  :root{
    --blue:#0292cd;
    --blue-mid:#33a6d7;
    --blue-light:#85cae6;
    --blue-deep:#3176b5;
    --ink:#333333;
    --ink-dark:#1b1b1b;
    --grey:#5c5c5c;
    --grey-mid:#474747;
    --white:#ffffff;
    --stage:#3d3d3d;
  }
  *{margin:0;padding:0;box-sizing:border-box}
  html,body{width:900px;height:1200px;overflow:hidden;background:var(--stage)}
  .flyer{position:absolute;left:95px;top:82px;width:724px;height:1025px;background:var(--white);overflow:hidden;font-family:"Lato",sans-serif;color:var(--ink)}
  .flyer-shapes{position:absolute;left:0;top:0}
  .brand{position:absolute;left:38px;top:368px;display:flex;align-items:center;gap:12px}
  .brand-dot{width:50px;height:50px;border-radius:50%;background:var(--blue-mid)}
  .brand-name{font-family:"Lato",sans-serif;font-weight:700;font-size:26px;color:var(--grey-mid)}
  .offer{position:absolute;text-align:center;font-family:"Arimo",sans-serif;color:var(--ink-dark)}
  .offer-led{left:350px;top:330px;width:190px}
  .offer-led .offer-title{font-size:29px;font-weight:700;color:var(--blue);letter-spacing:1px;line-height:1}
  .offer-led .offer-note{font-size:13.5px;margin-top:3px}
  .offer-terms{display:inline-block;margin-top:7px;background:var(--blue-mid);color:var(--ink-dark);font-size:14px;padding:2px 6px}
  .offer-discount{left:540px;top:270px;width:170px;font-size:14px;line-height:1.25}
  .offer-discount .offer-title{font-size:28px;font-weight:700;color:var(--blue);line-height:1}
  .headline{position:absolute;left:26px;top:540px;font-family:"Roboto Condensed",sans-serif;text-transform:uppercase}
  .headline-top{font-size:25px;font-weight:500;color:var(--ink-dark);letter-spacing:.3px}
  .headline-main{font-size:38px;font-weight:700;color:var(--blue-mid);margin-top:4px}
  .tagline{position:absolute;left:26px;top:624px;font-weight:700;font-size:18.5px;line-height:1.3;color:var(--ink-dark)}
  .phone{position:absolute;left:0;top:699px;width:240px;height:31px;background:var(--blue-mid);border-radius:0 16px 16px 0;color:var(--white);font-weight:700;font-size:21px;line-height:31px;padding-left:26px}
  .contact{position:absolute;left:28px;display:flex;align-items:center;gap:12px;font-size:18.5px;color:var(--ink-dark)}
  .contact-email{top:753px}
  .contact-social{top:788px}
  .contact-square{width:24px;height:24px;background:var(--blue-deep)}
  .divider{position:absolute;left:401px;top:502px;width:2px;height:456px;background:var(--grey)}
  .services{position:absolute;left:424px;top:489px;list-style:none}
  .services li{display:flex;align-items:center;height:29.3px;font-size:17.5px;color:var(--ink-dark)}
  .services svg{width:20px;height:18px;margin-right:10px;flex:none}
</style>
</head>
<body>
<div class="flyer">
  <svg class="flyer-shapes" width="724" height="1025" viewBox="0 0 724 1025">
    <defs>
      <linearGradient id="interiorTone" x1="0" y1="0" x2=".35" y2="1">
        <stop offset="0" stop-color="#f4f5f3"/>
        <stop offset=".4" stop-color="#ece7de"/>
        <stop offset=".7" stop-color="#d8ccbb"/>
        <stop offset="1" stop-color="#a99079"/>
      </linearGradient>
      <linearGradient id="poolTone" x1="0" y1="0" x2="1" y2="1">
        <stop offset="0" stop-color="#fbfbfb"/>
        <stop offset=".5" stop-color="#e9ebec"/>
        <stop offset="1" stop-color="#cfd3d5"/>
      </linearGradient>
      <linearGradient id="roomTone" x1="0" y1="0" x2="1" y2="1">
        <stop offset="0" stop-color="#eef0ef"/>
        <stop offset=".45" stop-color="#d3d8d0"/>
        <stop offset=".75" stop-color="#9fae8c"/>
        <stop offset="1" stop-color="#7a5e47"/>
      </linearGradient>
      <clipPath id="roomClip"><ellipse cx="155" cy="1050" rx="160" ry="192"/></clipPath>
    </defs>

    <polygon points="260,470 724,430 724,1025 230,1025 230,860 400,860 400,560" fill="url(#poolTone)" role="img" aria-label="Faded photo of a home pool and garden"/>
    <polygon points="0,530 360,420 724,440 724,470 0,560" fill="#f4f5f6"/>

    <polygon points="0,0 724,0 724,270 360,390 0,225" fill="url(#interiorTone)" role="img" aria-label="Photo of a bright modern living room with lounge and artwork"/>
    <polygon points="0,225 360,390 350,392 0,300" fill="var(--blue-mid)"/>
    <polygon points="705,285 724,280 724,335 705,340" fill="var(--blue-mid)"/>

    <circle cx="445" cy="360" r="110" fill="var(--white)" stroke="var(--ink-dark)" stroke-width="9"/>
    <circle cx="625" cy="320" r="95" fill="var(--white)" stroke="var(--ink-dark)" stroke-width="9"/>

    <rect x="0" y="850" width="310" height="175" fill="url(#roomTone)" clip-path="url(#roomClip)" role="img" aria-label="Photo of an open-plan room with air conditioner and garden view"/>
    <ellipse cx="155" cy="1050" rx="160" ry="192" fill="none" stroke="var(--ink-dark)" stroke-width="9"/>
  </svg>

  <div class="brand"><span class="brand-dot"></span><span class="brand-name">Tulven Electrics</span></div>

  <div class="offer offer-led">
    <div class="offer-title">FREE LED</div>
    <div class="offer-note">downlights on installation</div>
    <div class="offer-terms">Terms conditions apply</div>
  </div>
  <div class="offer offer-discount">
    <div class="offer-title">10% OFF</div>
    all electrical services<br>or<br>Free LED downlights<br>on installation
  </div>

  <div class="headline">
    <div class="headline-top">All Residential &amp; Commercial</div>
    <div class="headline-main">Electrical Services</div>
  </div>
  <p class="tagline">Specialising inNew homes&nbsp; renovations<br>and commercial projects</p>
  <div class="phone">ph-0437 619 458</div>
  <div class="contact contact-email"><span class="contact-square"></span>admin@tulvenelectrics.example.au</div>
  <div class="contact contact-social">
    <svg width="26" height="20" viewBox="0 0 26 20"><rect x="1" y="1" width="24" height="18" fill="none" stroke="var(--blue-mid)" stroke-width="2"/><path d="M1 1 L13 11 L25 1" fill="none" stroke="var(--blue-mid)" stroke-width="2"/></svg>
    facebook TulvenElectrics
  </div>

  <div class="divider"></div>
  <ul class="services">
    <li><svg viewBox="0 0 20 18"><path d="M1 9 L7 16 L19 1" fill="none" stroke="var(--blue)" stroke-width="3"/></svg>New Home installations</li>
    <li><svg viewBox="0 0 20 18"><path d="M1 9 L7 16 L19 1" fill="none" stroke="var(--blue)" stroke-width="3"/></svg>Commercial projects</li>
    <li><svg viewBox="0 0 20 18"><path d="M1 9 L7 16 L19 1" fill="none" stroke="var(--blue)" stroke-width="3"/></svg>Shop fit outs</li>
    <li><svg viewBox="0 0 20 18"><path d="M1 9 L7 16 L19 1" fill="none" stroke="var(--blue)" stroke-width="3"/></svg>Renovations</li>
    <li><svg viewBox="0 0 20 18"><path d="M1 9 L7 16 L19 1" fill="none" stroke="var(--blue)" stroke-width="3"/></svg>Smoke Detectors</li>
    <li><svg viewBox="0 0 20 18"><path d="M1 9 L7 16 L19 1" fill="none" stroke="var(--blue)" stroke-width="3"/></svg>Air Conditioning and Ceiling</li>
    <li><svg viewBox="0 0 20 18"><path d="M1 9 L7 16 L19 1" fill="none" stroke="var(--blue)" stroke-width="3"/></svg>Fans</li>
    <li><svg viewBox="0 0 20 18"><path d="M1 9 L7 16 L19 1" fill="none" stroke="var(--blue)" stroke-width="3"/></svg>Garden Lighting</li>
    <li><svg viewBox="0 0 20 18"><path d="M1 9 L7 16 L19 1" fill="none" stroke="var(--blue)" stroke-width="3"/></svg>Oven and Cooktop Installations</li>
    <li><svg viewBox="0 0 20 18"><path d="M1 9 L7 16 L19 1" fill="none" stroke="var(--blue)" stroke-width="3"/></svg>Power Point installation</li>
    <li><svg viewBox="0 0 20 18"><path d="M1 9 L7 16 L19 1" fill="none" stroke="var(--blue)" stroke-width="3"/></svg>LED lighting upgrades</li>
    <li><svg viewBox="0 0 20 18"><path d="M1 9 L7 16 L19 1" fill="none" stroke="var(--blue)" stroke-width="3"/></svg>Security Lighting</li>
    <li><svg viewBox="0 0 20 18"><path d="M1 9 L7 16 L19 1" fill="none" stroke="var(--blue)" stroke-width="3"/></svg>Switchboard upgrades</li>
    <li><svg viewBox="0 0 20 18"><path d="M1 9 L7 16 L19 1" fill="none" stroke="var(--blue)" stroke-width="3"/></svg>Test and Tag</li>
    <li><svg viewBox="0 0 20 18"><path d="M1 9 L7 16 L19 1" fill="none" stroke="var(--blue)" stroke-width="3"/></svg>Commercial Property</li>
    <li><svg viewBox="0 0 20 18"><path d="M1 9 L7 16 L19 1" fill="none" stroke="var(--blue)" stroke-width="3"/></svg>General Electrical Maintenance</li>
  </ul>
</div>
</body>
</html>
```